Web Design Project

Please design a new website template for Larkspurleigh as follows -

Existing Website - http://www.larkspurleigh.com.au/

Logo - http://brightquaydesk.com/Design/larkspurleigh-logo

Navigation - Top Horizontal

Colours: Pink and purple from attached logo (do not use the bright pink from the existing website)

Page Structure: Home, About Us, Services, The Team, Key Contacts, Our Values, Send Resume, Timesheets, Candidates, Clients, Location, Contact Us.

The template should include an enquiry from on all pages with fields: Name, Phone, Email, Enquiry

The template should include their phone number in the top right corner - (08) 9617 2259

It should include a tag line: Temporary & Permanent Support Staff Specialists

The Footer:
Level 5, 7 Tembley Parade
SUBIACO
WA 6008
Phone - (08) 9617 2259
Fax - (08) 9617 2271
Email - admin@larkspurleigh.com.au

Websites they like - http://www.dwightmorrowcosmeticclinic.com.au/ (preferably keep the text on a white background on this site)

Include a button/icon for - Job Listings

Home page text - Use what is on their existing website (you can reduce the number of bullet points)

Reason: I will review this job tomorrow and make a decision then, please upload psd files for all projects.

Reason: We have made a decisions, just waiting on some updates from your end.

Reason: I need the psd file please.

```html
<!DOCTYPE html>
<html lang="en">
<head>
<meta charset="utf-8">
<title>Larkspurleigh – The Recruitment Bureau</title>
<link rel="stylesheet" href="https://fonts.googleapis.com/css2?family=Marcellus&family=Open+Sans:wght@400;600&family=Roboto+Condensed:wght@400;700&family=Ubuntu:wght@400;500&display=swap">
<style>
:root{
  --pink:#e54b9b;
  --pink-deep:#c92c7e;
  --pink-text:#e0338a;
  --purple:#6a3b8c;
  --purple-dark:#5a2f78;
  --footer:#683a7e;
  --ink:#222;
  --white:#fff;
  --orange:#e8820c;
  --brand-ink:#1d1020;
}
*{box-sizing:border-box;margin:0;padding:0}
html,body{width:1200px;height:1114px;overflow:hidden}
body{position:relative;background:var(--pink);font-family:"Open Sans",Verdana,sans-serif;color:var(--ink)}
a{text-decoration:none;color:inherit}
.abs{position:absolute}

/* header */
.site-header{left:0;top:0;width:1200px;height:168px;background:var(--pink)}
.brand{left:166px;top:84px;display:flex;align-items:center;gap:12px}
.brand-mark{width:30px;height:30px;border-radius:50%;background:var(--purple)}
.brand-name{font-family:"Marcellus",serif;font-size:38px;line-height:40px;color:var(--brand-ink);letter-spacing:1px}
.util-links{right:163px;top:8px;display:flex;gap:26px;font-family:"Roboto Condensed",sans-serif;font-size:14px;color:var(--white)}
.util-links a{color:var(--white);display:flex;align-items:center;gap:5px}
.phone{right:163px;top:90px;display:flex;align-items:center;gap:10px}
.phone-number{font-family:"Roboto Condensed",sans-serif;font-weight:700;font-size:35px;color:var(--white);text-shadow:1px 2px 3px rgba(0,0,0,.35);letter-spacing:.5px}

/* hero */
.hero-band{left:0;top:170px;width:1200px;height:250px;background:linear-gradient(#fbd3e6,#e970ad)}
.hero-photo{left:144px;top:170px;width:912px;height:250px;background:linear-gradient(100deg,#dfe3ea 0%,#c9cfd9 40%,#8c95a4 70%,#b7bcc6 100%)}
.hero-caption{left:144px;top:385px;width:912px;height:35px;background:rgba(40,40,45,.55);color:var(--white);font-size:14px;letter-spacing:1px;text-align:center;line-height:35px}

/* nav */
.main-nav{left:0;top:420px;width:1200px;height:39px;background:linear-gradient(#e85ea5,#cf2f83);border-top:1px solid #f7a6cf;border-bottom:1px solid #f7a6cf}
.main-nav ul{list-style:none;display:flex;gap:19px;position:absolute;left:166px;top:9px}
.main-nav a{font-family:"Roboto Condensed",sans-serif;font-weight:700;font-size:15px;color:var(--white);letter-spacing:.2px}

/* content */
.content{left:144px;top:459px;width:912px;height:535px;background:linear-gradient(#ececec,#fafafa 40%,#fff)}
.tile{top:478px;width:202px;height:100px;background:linear-gradient(160deg,#7b4b9d,var(--purple) 50%,var(--purple-dark));border:2px solid #ec5ba8;border-radius:3px;box-shadow:0 6px 8px rgba(0,0,0,.15);display:flex;align-items:center;color:var(--white)}
.tile-icon{width:70px;height:64px;margin-left:12px;border-radius:8px}
.tile-label{font-family:"Ubuntu",sans-serif;font-size:20px;line-height:22px;color:var(--white);margin-left:22px;text-shadow:1px 1px 2px rgba(0,0,0,.4)}

.welcome-title{left:166px;top:601px;font-family:"Marcellus",serif;font-weight:400;font-size:23px;line-height:28px;color:var(--pink-text);white-space:nowrap}
.intro{left:166px;top:632px;width:600px;font-size:12px;line-height:17.5px}
.mission-title{left:166px;top:707px;font-size:13px;font-weight:400;color:var(--pink-text)}
.mission{left:166px;top:725px;width:610px;font-size:12px;line-height:17.5px}
.view-more{left:695px;top:788px;font-size:10px;color:var(--orange);display:flex;align-items:center;gap:3px}

.sectors{left:170px;top:826px;width:592px;height:141px;border:1px solid #cfcfcf;border-radius:4px;background:linear-gradient(#f8f8f8,#f1eef0);box-shadow:0 6px 8px rgba(0,0,0,.1)}
.sector-list{list-style:none;position:absolute;top:12px}
.sector-list li{font-size:13px;font-weight:600;color:var(--pink-text);height:24px;display:flex;align-items:center;gap:4px}
.sector-list li::before{content:"";width:6px;height:10px;border-left:3px solid var(--pink-deep);border-radius:4px 0 0 4px}

/* enquiry form */
.enquiry{left:791px;top:617px;width:239px;height:350px;background:linear-gradient(#e2e2e2,#f2f2f2);border:1px solid #d3d3d3;border-radius:4px;box-shadow:0 8px 10px rgba(0,0,0,.12)}
.enquiry-ribbon{left:814px;top:611px;width:194px;height:66px;background:linear-gradient(#fbc2df,#ef7cb8 45%,#e9549f);border-top:5px solid #444;border-radius:4px 4px 40% 40%/4px 4px 14px 14px;color:var(--white);font-family:"Roboto Condensed",sans-serif;font-size:19px;text-align:center;padding-top:21px;text-shadow:0 1px 2px rgba(0,0,0,.3)}
.enquiry-note{left:811px;top:686px;width:210px;font-size:12.5px;line-height:15.5px;color:var(--pink-text)}
.field{left:811px;width:203px;height:25px;background:var(--white);border:1px solid #cfcfcf;border-radius:4px;font-size:11px;color:#555;padding:5px 11px}
.field-message{height:63px}
.callback{left:827px;top:905px;width:168px;height:39px;background:linear-gradient(#ef5aa6,#c6186f);border-radius:4px;color:var(--white);font-family:"Ubuntu",sans-serif;font-size:17px;text-align:center;line-height:39px;box-shadow:0 3px 5px rgba(0,0,0,.25)}

/* footer */
.site-footer{left:0;top:994px;width:1200px;height:120px;background:var(--footer);color:var(--white);font-family:"Roboto Condensed",sans-serif;font-size:13px}
.footer-address{position:absolute;right:163px;top:13px;text-align:right;line-height:18.5px;font-style:normal}
.copyright{position:absolute;left:164px;top:87px}
</style>
</head>
<body>

<header class="site-header abs"></header>
<div class="brand abs">
  <span class="brand-mark"></span>
  <span class="brand-name">Larkspurleigh</span>
</div>
<nav class="util-links abs">
  <a href="#"><svg width="18" height="16" viewBox="0 0 18 16"><path d="M9 1 1 8h2.5v7h4v-5h3v5h4V8H17z" fill="#fff"/></svg>Home</a>
  <a href="#"><svg width="20" height="14" viewBox="0 0 20 14"><rect x="1" y="1" width="18" height="12" fill="#fff" stroke="#bbb"/><path d="M1 1l9 7 9-7" fill="none" stroke="#888"/></svg>Contact Us</a>
</nav>
<div class="phone abs">
  <svg width="86" height="56" viewBox="0 0 86 56"><path d="M4 20 58 2l26 26-54 22z" fill="#4f8a80" stroke="#2f5f57" stroke-width="2"/><path d="M30 22c6-6 18-9 24-4l-4 4c-4-2-10-1-14 3z" fill="#fff"/><rect x="34" y="24" width="16" height="10" rx="2" fill="#fff" transform="rotate(-18 42 29)"/></svg>
  <span class="phone-number">(08) 9617 2259</span>
</div>

<div class="hero-band abs"></div>
<div class="hero-photo abs" role="img" aria-label="Photo of smiling office staff in a business meeting"></div>
<p class="hero-caption abs">Temporary &amp; Permanent Support Staff Specialists</p>

<nav class="main-nav abs">
  <ul>
    <li><a href="#">ABOUT US</a></li>
    <li><a href="#">SERVICES</a></li>
    <li><a href="#">THE TEAM</a></li>
    <li><a href="#">KEY CONTACTS</a></li>
    <li><a href="#">OUR VALUES</a></li>
    <li><a href="#">SEND RESUME</a></li>
    <li><a href="#">TIMESHEETS</a></li>
    <li><a href="#">CANDIDATES</a></li>
    <li><a href="#">CLIENTS</a></li>
    <li><a href="#">LOCATION</a></li>
  </ul>
</nav>

<main class="content abs"></main>

<a class="tile abs" style="left:164px" href="#"><span class="tile-icon" role="img" aria-label="Checklist document with pen illustration" style="background:#e6e6ea"></span><span class="tile-label">Job<br>Listing</span></a>
<a class="tile abs" style="left:388px" href="#"><span class="tile-icon" role="img" aria-label="Globe with form illustration" style="background:linear-gradient(135deg,#3f7fc4,#5aa04a)"></span><span class="tile-label">Services</span></a>
<a class="tile abs" style="left:611px" href="#"><span class="tile-icon" role="img" aria-label="Green contacts book illustration" style="background:#3f9a3a"></span><span class="tile-label">Key<br>Contacts</span></a>
<a class="tile abs" style="left:834px" href="#"><span class="tile-icon" role="img" aria-label="Green folder with globe illustration" style="background:#6ccf3e"></span><span class="tile-label">Our<br>Values</span></a>

<h1 class="welcome-title abs">Welcome to Larkspurleigh - The Recruitment Bureau</h1>
<p class="intro abs">Larkspurleigh has impeccable credentials. Our experienced and thoroughly professional team services a broad range of blue-chip national and multi-national companies with the recruitment of temporary and permanent staff in the areas of:</p>
<h2 class="mission-title abs">Our Mission</h2>
<p class="mission abs">To be the recruitment company of choice. To work together with our clients to provide services that are seen as creative and value-for-money. To be recognised and respected both within our own industry and that of our clients; and to consistently demonstrate our professionalism and passion for business</p>
<a class="view-more abs" href="#">View more <svg width="12" height="9" viewBox="0 0 12 9"><path d="M0 0l5 4.5L0 9zM6 0l5 4.5L6 9z" fill="#e8820c"/></svg></a>

<section class="sectors abs">
  <ul class="sector-list" style="left:51px">
    <li>Administration</li><li>Personal Assistant</li><li>Executive Assistant</li><li>Reception</li><li>Legal</li>
  </ul>
  <ul class="sector-list" style="left:341px">
    <li>Secretaries</li><li>Accounts Clerk</li><li>Project Engineering</li><li>Construction and Property</li><li>Project Engineering</li>
  </ul>
</section>

<aside class="enquiry abs"></aside>
<div class="enquiry-ribbon abs">FIND OUT MORE</div>
<p class="enquiry-note abs">Complete this form and &nbsp;we"ll get back to you within 24 hours to answer your questions.</p>
<div class="field abs" style="top:738px">Name</div>
<div class="field abs" style="top:769px">Phone</div>
<div class="field abs" style="top:804px">Email</div>
<div class="field field-message abs" style="top:837px">Message</div>
<div class="callback abs">Request a Call Back</div>

<footer class="site-footer abs">
  <address class="footer-address">Level 5, 7 Tembley Parade<br>HOLLOWMERE, WA 6091<br>Phone - (08) 9617 2259<br>Fax - (08) 9617 2271<br>Email - admin@larkspurleigh.com.au</address>
  <p class="copyright">© 2012 Larkspurleigh - The Recruitment Bureau</p>
</footer>

</body>
</html>
```